Australian HR Consultancy Company Brochure (and more!). Our tagline "Start something amazing."

We are a start-up HR and Recruitment consultancy. We have a group of young, passionate and top performing staff who assist companies with driving their workforce productivity, keeping employees happy, hiring fantastic people and ensuring legal compliance across the HR field.

We work across a variety of sectors such as mining, Not for Profits, Finance, Accounting, Health etc so are not pigeon-holed to one particular group. We tend to deal with medium sized businesses.

Our team is professional and corporate but down to earth and approachable. We have unique offerings in terms of our services and our pricing. We deliver exceptional value to our clients and build long term mutually beneficial relationships. We care about giving back to the community and doing the right thing by everyone we deal with.

Our design should communicate that we are corporate and professional but not uptight 'suits', that we are fresh and engaging. Clear, concise, crisp but not cold.

Thinking 6 page brochure.

We have a variety of colours in our logo and tend to lean towards fresh shades of blue and green but are definitely open to other colours such as purple, pink, orange etc. We would prefer the brochure to be in landscape format (like a powerpoint presentation) as apparently that's easier to read? but open to your expert suggestions!

Target Market(s)

Medium sized business across all industries but within the professional area ie finance, mining, health.

Industry/Entity Type

It Company

Colors
33b8a4
33a6d7
0592cd
85cae6
86cfc6
b768aa

Requirements
Must have
• Needs to be editable version as we will be changing our tagline and about us in the new year.

```html
<!DOCTYPE html>
<html lang="en">
<head>
<meta charset="utf-8">
<title>TeamBegin – Brochure Pages</title>
<link href="https://fonts.googleapis.com/css2?family=PT+Sans:wght@400;700&display=swap" rel="stylesheet">
<style>
  :root{
    --backdrop:#e9e6e1;
    --paper:#ffffff;
    --ink:#2b2f3a;
    --ink-soft:#444a57;
    --brand:#2f3542;
    --accent-teal:#33b8a4;
    --accent-blue:#0592cd;
    --accent-sky:#85cae6;
    --accent-purple:#b768aa;
    --photo-yellow:#f3ebb5;
    --photo-lilac:#c8b9da;
    --photo-violet:#7b78a3;
    --photo-grey:#a9b4bd;
  }
  *{box-sizing:border-box;margin:0;padding:0}
  html,body{width:960px;height:1200px;overflow:hidden}
  body{background:var(--backdrop);font-family:"PT Sans",Arial,sans-serif;color:var(--ink);position:relative}

  .page{position:absolute;width:410px;height:307px;background:var(--paper);overflow:hidden;box-shadow:0 4px 10px rgba(0,0,0,.25)}
  .col-left{left:58px}.col-right{left:494px}
  .row-1{top:76px}.row-2{top:414px}.row-3{top:752px}

  .brand{position:absolute;left:20px;top:20px;display:flex;align-items:center;gap:6px;font-weight:700;font-size:14px;color:var(--brand);z-index:2}
  .brand-dot{width:14px;height:14px;border-radius:50%;background:var(--accent-blue)}
  .tagline{position:absolute;right:22px;top:24px;font-size:8.5px;letter-spacing:3.2px;color:var(--ink);z-index:2}

  .content{position:absolute;left:22px;right:22px;z-index:2}
  h2{font-size:13px;font-weight:700;color:var(--ink);margin-bottom:10px}
  p{font-size:7.6px;line-height:1.4;color:var(--ink-soft);margin-bottom:8px}
  .lead{font-size:8px;color:var(--ink)}
  .lead b{font-weight:700}
  .bullets{display:flex;gap:22px;margin-bottom:8px}
  ul{list-style:none;font-size:6.6px;line-height:1.3;color:var(--ink-soft)}
  li{position:relative;padding-left:12px}
  li::before{content:"";position:absolute;left:2px;top:3.5px;width:2px;height:2px;border-radius:50%;background:var(--ink)}

  .photo{position:absolute;left:0;right:0;bottom:0;z-index:1;
    background:linear-gradient(to bottom,rgba(255,255,255,0) 0%,var(--photo-yellow) 30%,var(--photo-lilac) 72%,var(--photo-violet) 100%)}

  /* cover */
  .cover{background:linear-gradient(155deg,#cfd6da 0%,#b5bcc2 35%,#d9d1a8 62%,#b4a7c8 85%,#8a86ad 100%)}
  .cover .brand{left:46px;top:48px;font-size:20px}
  .cover .brand-dot{width:20px;height:20px}
  .cover .tagline{left:30px;right:auto;top:104px;font-size:9px;letter-spacing:3.4px}

  .team{position:absolute;left:0;right:0;top:156px;text-align:center;z-index:2}
  .team h3{font-size:9px;font-weight:700;margin-bottom:6px}
  .team-row{display:flex;justify-content:center;gap:14px;margin-left:4px}
  .member{width:66px;text-align:center;font-size:8px;font-weight:700}
  .portrait{width:66px;height:66px;border-radius:50%;border:3px solid #fff;background:linear-gradient(160deg,#c7bfb4,#8c8276);margin-bottom:4px;box-shadow:0 1px 3px rgba(0,0,0,.25)}
  .contact-line{font-size:7.6px;color:var(--ink-soft);margin-bottom:6px}
</style>
</head>
<body>

<section class="page cover col-left row-1" role="img" aria-label="Cover photo: two businessmen reviewing a tablet together in a bright office">
  <div class="brand"><span class="brand-dot"></span>TeamBegin</div>
  <div class="tagline">Start something amazing</div>
</section>

<section class="page col-right row-1">
  <div class="brand"><span class="brand-dot"></span>TeamBegin</div>
  <div class="tagline">Start something amazing</div>
  <div class="content" style="top:78px">
    <h2>About Us</h2>
    <p>TeamBegin is an innovative industry leader in the provision of human resources, industrial relations and recruitment managed services. Our unique approach enables us to meet the challenges and demands of a diverse group of a contemporary Australian businesses.</p>
    <p>We are committed to delivering exceptional service and value that ensures the best outcomes for our long-term business partnerships.</p>
  </div>
  <div class="photo" style="top:180px" role="img" aria-label="Photo: hands holding a pen over a tablet on a meeting table"></div>
</section>

<section class="page col-left row-2">
  <div class="brand"><span class="brand-dot"></span>TeamBegin</div>
  <div class="tagline">Start something amazing</div>
  <div class="content" style="top:64px">
    <h2>HR Consulting</h2>
    <p class="lead"><b>HR Foundations -</b> Building the HR foundations for legal compliance &amp; employee management</p>
    <div class="bullets">
      <ul><li>Employment Contracts &amp; Agreements</li><li>Organisational Structure&amp; Design</li><li>Terminations &amp; Fair Work Advice</li><li>Performance Management</li></ul>
      <ul><li>Recruitment &amp; Onboarding</li><li>Remuneration &amp; Benefits</li><li>HR Policies &amp; Procedures</li><li>Workplace Investigations</li></ul>
    </div>
    <p class="lead"><b>Strategic HR -</b> Driving organisational success through strategic people design</p>
    <ul><li>Leadership Development</li><li>Organisational Design</li><li>Change Management</li><li>Culture Programs</li><li>Organisational Capabilities</li><li>Executive&amp; Leadership Coaching</li><li>Employee Engagement &amp; Retention</li><li>Talent Attraction &amp; Acquisition</li></ul>
  </div>
  <div class="photo" style="top:150px" role="img" aria-label="Photo: two women smiling while working together at a laptop"></div>
</section>

<section class="page col-right row-2">
  <div class="brand"><span class="brand-dot"></span>TeamBegin</div>
  <div class="tagline">Start something amazing</div>
  <div class="content" style="top:80px">
    <h2>Professional Staffing - Start Hiring Incredible People</h2>
    <p class="lead">Matching great organisations to great people.</p>
    <div class="bullets">
      <ul><li>Executive Search</li><li>Recruitment Processing Outsourcing (RPO)</li><li>Contingent &amp; Retained Services</li><li>Permanent Recruitment</li></ul>
      <ul><li>Recruitment Admin Support</li><li>Manager Interview Training</li><li>Talent Attraction &amp; Acquisition Programs</li><li>xxxx</li></ul>
    </div>
  </div>
  <div class="photo" style="top:150px" role="img" aria-label="Photo: row of candidates seated on chairs waiting for interviews"></div>
</section>

<section class="page col-left row-3">
  <div class="brand"><span class="brand-dot"></span>TeamBegin</div>
  <div class="tagline">Start something amazing</div>
  <div class="content" style="top:78px">
    <h2>Workshops - Let’s Start Developing Your Team</h2>
    <p class="lead">Customised programs designed to make a strategic impact on your organisation and leadership.</p>
    <p style="font-size:6.6px;margin-left:6px">Presented as 1-1.5 hour ‘Lunch ‘N’ Learns’, half day or full day workshops as requested across:</p>
    <div class="bullets" style="gap:52px">
      <ul><li>Leadership Development</li><li>Team Building</li><li>Change Management</li></ul>
      <ul><li>Culture Building</li><li>Management Basics</li></ul>
    </div>
  </div>
  <div class="photo" style="top:160px" role="img" aria-label="Photo: presenter speaking to a seated workshop group"></div>
</section>

<section class="page col-right row-3">
  <div class="brand"><span class="brand-dot"></span>TeamBegin</div>
  <div class="tagline">Start something amazing</div>
  <div class="content" style="top:78px">
    <h2>Start a Conversation with Us</h2>
    <div class="contact-line">www.teambegin.example</div>
    <div class="contact-line">Ph: 1300 555 018</div>
  </div>
  <div class="photo" style="top:120px" role="img" aria-label="Photo: bright open-plan office in soft focus"></div>
  <div class="team">
    <h3>Our Leadership Team</h3>
    <div class="team-row">
      <div class="member"><div class="portrait" role="img" aria-label="Portrait of Ben"></div>Ben</div>
      <div class="member"><div class="portrait" role="img" aria-label="Portrait of Clara"></div>Clara</div>
      <div class="member"><div class="portrait" role="img" aria-label="Portrait of Maya"></div>Maya</div>
    </div>
  </div>
</section>

</body>
</html>
```